Startup of Management Company looking for Designers!

I am looking for an upscale website. Valmoreth will focus on Real Estate, Wealth Management, and Consulting,

Target Market(s)

investors, sellers of real estate, people looking to have their real estate management.
companies looking for consulting services

Number of Pages Required

5+ page

Font styles to use
Sans Serif

Requirements
Must have
• pictures, real.

```html
<!DOCTYPE html>
<html lang="en">
<head>
<meta charset="utf-8">
<title>Valmoreth Real Estate Management</title>
<link rel="stylesheet" href="https://fonts.googleapis.com/css2?family=Mulish:ital,wght@0,400;0,500;0,600;0,700;0,800;1,400&display=swap">
<style>
:root{
  --blue:#16a2d9;
  --blue-bar:#0bb1e7;
  --ink:#111;
  --text:#2a2a2a;
  --muted:#555;
  --grey-bg:#f3f3f3;
  --frame:#c3c3c3;
  --white:#fff;
  --black:#000;
}
*{margin:0;padding:0;box-sizing:border-box}
html,body{width:1200px;height:4244px;overflow:hidden}
body{position:relative;background:var(--white);font-family:"Mulish",Arial,sans-serif;color:var(--text)}
.abs{position:absolute}
/* header */
.site-header{top:0;left:0;width:1200px;height:76px;background:var(--white)}
.brand{left:143px;top:16px}
.brand-name{font-size:29px;font-weight:500;color:var(--ink);letter-spacing:.5px;line-height:1}
.brand-tag{font-size:12px;color:var(--blue);margin-top:3px;padding-left:11px}
.nav a{position:absolute;top:34px;font-size:14px;color:var(--ink);text-decoration:none}
.nav a.active{color:var(--blue)}
/* hero */
.hero{top:76px;left:0;width:1200px;height:496px;background:linear-gradient(180deg,#5f6f7a 0%,#76848c 25%,#4c5760 55%,#3c454d 100%)}
.hero-shade{inset:0;background:rgba(0,0,0,.18)}
.hero-title{top:170px;left:0;width:1200px;text-align:center;color:var(--white);font-size:36px;font-weight:600;line-height:44px}
.btn{display:block;position:absolute;background:var(--black);color:var(--blue);font-size:15px;font-weight:500;text-align:center;text-decoration:none}
.hero .btn{left:519px;top:277px;width:160px;height:38px;line-height:36px;border:1px solid var(--white)}
/* about */
.about-photo{left:142px;top:697px;width:380px;height:394px;background:linear-gradient(135deg,#c8cdd3 0%,#e9ecee 45%,#9aa4b2 100%)}
.about-card{left:522px;top:809px;width:536px;height:366px;background:var(--white);box-shadow:0 2px 14px rgba(0,0,0,.12);padding:48px 38px 0 38px}
.about-card h2{font-size:38px;font-weight:500;color:var(--blue);line-height:46px;margin-bottom:12px}
.about-card p{font-size:12.5px;line-height:23px;color:var(--text);margin-bottom:10px}
.about-card .btn{left:40px;top:269px;width:127px;height:36px;line-height:36px}
/* mission */
.mission-ghost{left:333px;top:1270px;font-size:100px;font-weight:800;color:#f5f5f5;letter-spacing:2px;line-height:1}
.mission-title{left:227px;top:1309px;font-size:32px;font-weight:800;color:var(--ink)}
.mission-rule{left:474px;top:1300px;width:14px;height:54px}
.mission-text{left:521px;top:1274px;width:470px;font-size:12.5px;line-height:24px}
.mission-text b{color:var(--blue);font-weight:400}
.mission-sign{left:522px;top:1356px;font-size:13.5px;color:var(--blue)}
/* services */
.services{left:0;top:1445px;width:1200px;height:1493px;background:var(--grey-bg)}
.section-title{position:absolute;left:0;width:1200px;text-align:center;font-size:40px;font-weight:500;color:var(--ink)}
.underline{position:absolute;left:574px;width:52px;height:8px}
.svc-title{font-size:33px;font-weight:500;color:var(--blue)}
.svc-text{width:340px;font-size:12.5px;line-height:23px;color:var(--text)}
.svc-frame{border:6px solid var(--frame)}
.svc-photo{box-shadow:0 4px 14px rgba(0,0,0,.18)}
.svc .btn{width:127px;height:38px;line-height:38px}
/* why */
.why-item{width:200px;text-align:center;font-size:12.5px;line-height:17px;color:var(--text)}
.why-item svg{display:block;margin:0 auto 10px}
/* reviews */
.quote{left:234px;top:3575px;width:745px;text-align:center;font-style:italic;font-size:13px;line-height:24px;color:var(--muted)}
.qmark{font-size:38px;color:#bbb;font-family:Georgia,serif;line-height:1}
.reviewer{left:0;width:1200px;text-align:center}
.dot{position:absolute;top:3726px;width:7px;height:7px;border-radius:50%;background:#999}
/* footer */
.footer{left:0;top:3830px;width:1200px;height:358px;background:var(--black);color:var(--white)}
.footer h4{position:absolute;font-size:16px;font-weight:400;color:var(--blue)}
.footer .fline{position:absolute;height:2px;width:30px;background:var(--blue)}
.f-brand{left:152px;top:138px;text-align:center;width:204px}
.f-brand .brand-name{color:var(--white);font-size:35px}
.f-brand .brand-tag{font-size:14px;padding:0}
.social{position:absolute;top:214px;width:30px;height:30px;border:1px solid #777}
.social i{position:absolute;left:9px;top:9px;width:10px;height:10px;background:#bbb}
.f-list{position:absolute;left:428px;top:128px;list-style:none;font-size:12.5px;line-height:28px}
.f-list li::before{content:"• "}
.f-contact{position:absolute;font-size:12.5px;line-height:18px}
.f-icon{position:absolute;left:569px;width:28px;height:28px;border:1.5px solid var(--blue);border-radius:50%}
.hours{position:absolute;left:822px;top:130px;font-size:12.5px;line-height:18px}
.hours p{margin-bottom:18px}
.copyright{left:0;top:4188px;width:1200px;height:56px;background:var(--blue-bar);color:var(--white);text-align:center;font-size:12.5px;line-height:56px}
</style>
</head>
<body>

<header class="abs site-header">
  <div class="abs brand">
    <div class="brand-name">VALMORETH</div>
    <div class="brand-tag">Real Estate Management</div>
  </div>
  <nav class="nav">
    <a class="active" style="left:539px">Home</a>
    <a style="left:643px">Services</a>
    <a style="left:761px">About Us</a>
    <a style="left:887px">FAQs</a>
    <a style="left:985px">Contact Us</a>
  </nav>
</header>

<section class="abs hero" role="img" aria-label="Aerial photograph of a harbour city skyline with high-rise towers">
  <div class="abs hero-shade"></div>
  <h1 class="abs hero-title">Valmoreth Will Focus On<br>Real Estate, Wealth Management, And Consulting,</h1>
  <a class="btn">Contact Us Today</a>
</section>

<div class="abs about-photo" role="img" aria-label="Photograph of a smiling businesswoman in a striped shirt"></div>
<div class="abs about-card">
  <h2>About Valmoreth</h2>
  <p>Lorem ipsum dolor sit amet, consectetuer adipiscing elit, sed diam nonummy nibh euismod tincidunt ut laoreet dolore magna aliquam erat volutpat. Ut wisi enim ad minim veniam, quis nostrud exerci tation ullamcorper suscipit lobortis nisl ut aliquip ex ea commodo consequat. Duis autem vel eum</p>
  <p>Iriure dolor in hendrerit in vulputate velit esse molestie consequat, vel illum dolore eu feugiat nulla facilisis at vero eros et accumsan et iusto odio dignissim.</p>
  <a class="btn">Know More</a>
</div>

<div class="abs mission-ghost">MISSION</div>
<div class="abs mission-title">OUR MISSION</div>
<svg class="abs mission-rule" viewBox="0 0 14 54"><line x1="3" y1="8" x2="3" y2="46" stroke="#16a2d9" stroke-width="1.5"/><line x1="8" y1="0" x2="8" y2="54" stroke="#16a2d9" stroke-width="1.5"/><line x1="12" y1="14" x2="12" y2="40" stroke="#16a2d9" stroke-width="1"/></svg>
<p class="abs mission-text"><b>Our Mission</b> Lorem ipsum dolor sit amet, consectetuer adipiscing elit, sed diam nonummy nibh euismod tincidunt ut laoreet dolore magna aliquam erat volutpat. Ut wisi enim ad minim veniam, quis nostrud exerci tation .</p>
<div class="abs mission-sign">A Message From Ren Alcott</div>

<section class="abs services">
  <h2 class="section-title" style="top:60px">Our Services</h2>
  <svg class="underline" style="top:118px" viewBox="0 0 52 8"><line x1="0" y1="2" x2="52" y2="2" stroke="#16a2d9" stroke-width="1.5"/><line x1="8" y1="6" x2="44" y2="6" stroke="#16a2d9" stroke-width="1.5"/></svg>
</section>

<div class="svc">
  <div class="abs svc-frame" style="left:628px;top:1646px;width:465px;height:356px"></div>
  <div class="abs svc-photo" role="img" aria-label="Photograph of a handshake over a contract, pen and small model house" style="left:590px;top:1681px;width:466px;height:288px;background:linear-gradient(135deg,#3c3a38 0%,#8a8684 40%,#d9d6d2 70%,#5a4a3c 100%)"></div>
  <h3 class="abs svc-title" style="left:143px;top:1704px">Real Estate</h3>
  <p class="abs svc-text" style="left:145px;top:1752px">Lorem ipsum dolor sit amet, consectetuer adipiscing elit, sed diam nonummy nibh euismod tincidunt ut laoreet dolore magna aliquam erat volutpat. Ut wisi enim ad minim veniam, quis nostrud exerci tation ullamcorper suscipit lobortis nisl ut aliquip ex ea commod consequat. Duis autem vel eum</p>
  <a class="btn" style="left:145px;top:1898px">Know More</a>

  <div class="abs svc-frame" style="left:104px;top:2078px;width:466px;height:356px"></div>
  <div class="abs svc-photo" role="img" aria-label="Photograph of a hand on a laptop with glowing financial charts" style="left:142px;top:2114px;width:466px;height:287px;background:linear-gradient(135deg,#cfe0f0 0%,#6d93c0 40%,#2d4f86 75%,#1a2c55 100%)"></div>
  <h3 class="abs svc-title" style="left:649px;top:2136px">Wealth Management</h3>
  <p class="abs svc-text" style="left:649px;top:2184px">Lorem ipsum dolor sit amet, consectetuer adipiscing elit, sed diam nonummy nibh euismod tincidunt ut laoreet dolore magna aliquam erat volutpat. Ut wisi enim ad minim veniam, quis nostrud exerci tation ullamcorper suscipit lobortis nisl ut aliquip ex ea commod consequat. Duis autem vel eum</p>
  <a class="btn" style="left:649px;top:2332px">Know More</a>

  <div class="abs svc-frame" style="left:628px;top:2510px;width:465px;height:356px"></div>
  <div class="abs svc-photo" role="img" aria-label="Photograph of three colleagues working together at a laptop in an office" style="left:590px;top:2545px;width:466px;height:288px;background:linear-gradient(135deg,#5b6066 0%,#9ea6ad 40%,#e3e6e8 70%,#7c8590 100%)"></div>
  <h3 class="abs svc-title" style="left:143px;top:2568px">Business Consulting</h3>
  <p class="abs svc-text" style="left:145px;top:2616px">Lorem ipsum dolor sit amet, consectetuer adipiscing elit, sed diam nonummy nibh euismod tincidunt ut laoreet dolore magna aliquam erat volutpat. Ut wisi enim ad minim veniam, quis nostrud exerci tation ullamcorper suscipit lobortis nisl ut aliquip ex ea commod consequat. Duis autem vel eum</p>
  <a class="btn" style="left:143px;top:2764px">Know More</a>
</div>

<h2 class="section-title" style="top:2995px">Why Choose Us</h2>
<svg class="underline" style="top:3060px" viewBox="0 0 52 8"><line x1="0" y1="2" x2="52" y2="2" stroke="#16a2d9" stroke-width="1.5"/><line x1="8" y1="6" x2="44" y2="6" stroke="#16a2d9" stroke-width="1.5"/></svg>

<div class="abs why-item" style="left:147px;top:3120px">
  <svg width="66" height="66" viewBox="0 0 66 66" fill="none" stroke="#16a2d9" stroke-width="2" stroke-linecap="round"><path d="M33 14a14 14 0 0 0-8 25v7h16v-7a14 14 0 0 0-8-25z"/><line x1="26" y1="51" x2="40" y2="51"/><line x1="28" y1="56" x2="38" y2="56"/><line x1="33" y1="2" x2="33" y2="8"/><line x1="12" y1="12" x2="16" y2="16"/><line x1="54" y1="12" x2="50" y2="16"/><line x1="4" y1="30" x2="10" y2="30"/><line x1="56" y1="30" x2="62" y2="30"/><line x1="10" y1="46" x2="15" y2="42"/><line x1="56" y1="46" x2="51" y2="42"/></svg>
  Superior Advice For<br>Customers
</div>
<div class="abs why-item" style="left:394px;top:3120px">
  <svg width="66" height="66" viewBox="0 0 66 66" fill="none" stroke="#16a2d9" stroke-width="2" stroke-linejoin="round"><path d="M12 14l8-4 7 12-5 4c3 7 8 12 15 15l4-5 12 7-4 8C30 52 10 32 12 14z"/><path d="M34 6h24a4 4 0 0 1 4 4v12a4 4 0 0 1-4 4H44l-6 6v-6h-4a4 4 0 0 1-4-4V10a4 4 0 0 1 4-4z"/><circle cx="40" cy="16" r="1.5"/><circle cx="46" cy="16" r="1.5"/><circle cx="52" cy="16" r="1.5"/></svg>
  Unbiased<br>Recommendations
</div>
<div class="abs why-item" style="left:625px;top:3120px">
  <svg width="66" height="66" viewBox="0 0 66 66" fill="none" stroke="#16a2d9" stroke-width="2"><rect x="6" y="10" width="46" height="42" rx="3"/><line x1="6" y1="20" x2="52" y2="20"/><line x1="16" y1="4" x2="16" y2="14"/><line x1="42" y1="4" x2="42" y2="14"/><rect x="12" y="26" width="8" height="7"/><rect x="24" y="26" width="8" height="7"/><rect x="12" y="38" width="8" height="7"/><rect x="24" y="38" width="8" height="7"/><circle cx="50" cy="48" r="12" fill="#fff"/><path d="M50 41v7h6"/></svg>
  Considerable Time<br>For You
</div>
<div class="abs why-item" style="left:862px;top:3120px">
  <svg width="66" height="66" viewBox="0 0 66 66" fill="none" stroke="#16a2d9" stroke-width="2"><circle cx="22" cy="18" r="8"/><path d="M8 44c0-9 6-14 14-14s14 5 14 14z"/><circle cx="44" cy="30" r="8"/><path d="M30 58c0-9 6-14 14-14s14 5 14 14z"/><path d="M42 6h16v10h-6l-4 4v-4h-6z"/></svg>
  Deep Legal Industry<br>Relationships
</div>
<a class="btn" style="left:521px;top:3268px;width:161px;height:38px;line-height:38px">Contact Us Today</a>

<h2 class="section-title" style="top:3464px">Customer Reviews</h2>
<svg class="underline" style="top:3528px" viewBox="0 0 52 8"><line x1="0" y1="2" x2="52" y2="2" stroke="#16a2d9" stroke-width="1.5"/><line x1="8" y1="6" x2="44" y2="6" stroke="#16a2d9" stroke-width="1.5"/></svg>

<svg class="abs" style="left:152px;top:3596px" width="26" height="46" viewBox="0 0 26 46" fill="none" stroke="#999" stroke-width="1.5"><polyline points="22,2 4,23 22,44"/></svg>
<svg class="abs" style="left:1004px;top:3596px" width="26" height="46" viewBox="0 0 26 46" fill="none" stroke="#999" stroke-width="1.5"><polyline points="4,2 22,23 4,44"/></svg>
<div class="abs qmark" style="left:208px;top:3568px">&ldquo;</div>
<p class="abs quote">Lorem ipsum dolor sit amet, consectetuer adipiscing elit, sed diam nonummy nibh euismod tinciduntol ut laoreet dolore magna aliquam erat volutpat. Ut wisi enim ad minim veniam, quis nostrud exercimori mornkle tation ullamcorper suscipit lobortis nisl ut aliquip ex ea commodo consequat.</p>
<div class="abs qmark" style="left:753px;top:3632px">&rdquo;</div>
<div class="abs reviewer" style="top:3663px;font-size:15px;font-weight:600;color:var(--blue)">Mara T.</div>
<div class="abs reviewer" style="top:3684px;font-size:13px;color:var(--ink)">Harbor Point, CA</div>
<span class="dot" style="left:567px;background:var(--blue)"></span>
<span class="dot" style="left:581px"></span>
<span class="dot" style="left:595px"></span>
<span class="dot" style="left:609px"></span>

<footer class="abs footer">
  <div class="abs f-brand">
    <div class="brand-name">VALMORETH</div>
    <div class="brand-tag">Real Estate Management</div>
  </div>
  <span class="social" style="left:185px"><i></i></span>
  <span class="social" style="left:222px"><i></i></span>
  <span class="social" style="left:259px"><i></i></span>
  <span class="social" style="left:295px"><i></i></span>

  <h4 style="left:428px;top:76px">Quick Links</h4><span class="fline" style="left:428px;top:102px"></span>
  <ul class="f-list"><li>Home</li><li>Services</li><li>About Us</li><li>FAQs</li><li>Contact Us</li></ul>

  <h4 style="left:570px;top:76px">Contact Details</h4><span class="fline" style="left:570px;top:102px"></span>
  <span class="f-icon" style="top:124px"><svg width="25" height="25" viewBox="0 0 25 25" fill="none" stroke="#16a2d9" stroke-width="1.3"><path d="M12.5 19s-5-5-5-8.5a5 5 0 0 1 10 0c0 3.5-5 8.5-5 8.5z"/><circle cx="12.5" cy="10.5" r="1.8"/></svg></span>
  <div class="f-contact" style="left:610px;top:130px">Valmoreth<br>Street Name, City Name<br>State Zipcode</div>
  <span class="f-icon" style="top:207px"><svg width="25" height="25" viewBox="0 0 25 25" fill="none" stroke="#16a2d9" stroke-width="1.3"><path d="M7 6l3-1 2 4-2 1.5c1 2.5 2.5 4 5 5l1.5-2 4 2-1 3C12 18 7 13 7 6z"/></svg></span>
  <div class="f-contact" style="left:610px;top:213px">555.014.2290</div>
  <span class="f-icon" style="top:256px"><svg width="25" height="25" viewBox="0 0 25 25" fill="none" stroke="#16a2d9" stroke-width="1.3"><rect x="6" y="8" width="13" height="9"/><polyline points="6,8 12.5,13 19,8"/></svg></span>
  <div class="f-contact" style="left:610px;top:262px">inquiry@valmoreth.com</div>

  <h4 style="left:822px;top:76px">Working Hours</h4><span class="fline" style="left:822px;top:102px"></span>
  <div class="hours">
    <p>Mondays and Wednesdays - Friday<br>08:00 – 12:00 / 13:00 – 17:00</p>
    <p>Tuesday<br>08:00 – 12:00 / 13:00 – 19:00</p>
    <p>Saturdays &amp; Sunday<br>By Appointment Only</p>
  </div>
</footer>
<div class="abs copyright">Copyright © 2021 Valmoreth Real Estate Management. All Rights Reserved.</div>

</body>
</html>
```